Web Site

Target Market(s)

CEOs and International Sales & Marketing Directors of International Companies who wish to expand their business reach to Dubai and the Middle East and are looking for a local professional partner to work with.

Requirements
Must have
• Creativity is key. We don't want the normal standard boxes of text and boxes of pics. Be as creative as you like.
Nice to have
• (This is only a suggestion, we welcome your creativity)
- The center of all pages could be large rotating pictures which display professional corporate men/women working in an office, images of Dubai, the UAE, skyscrapers of business towers in Dubai, ..etc.
- Images should reflect Dubai and the Arab World as a modern, fast-paced, growing modern market - Not Traditional)
Should not have
• Not so colorful, the fewer colors you use, the better.
Not Crammed or Busy
Not Traditional but modern

```html
<!DOCTYPE html>
<html lang="en">
<head>
<meta charset="utf-8">
<title>Arbor Group</title>
<link href="https://fonts.googleapis.com/css2?family=Open+Sans:wght@400;600;700&display=swap" rel="stylesheet">
<style>
  :root {
    --bg-top: #f4f5f6;
    --bg-bottom: #e5e6e7;
    --page: #ffffff;
    --frame: #d6d6d6;
    --ink: #222222;
    --text: #444444;
    --nav: #333333;
    --accent: #8b2a2a;
    --badge: #b24848;
    --rule: #e2e2e2;
    --footer: #262626;
  }
  * { margin: 0; padding: 0; box-sizing: border-box; }
  html, body { width: 1200px; height: 900px; overflow: hidden; }
  body {
    background: linear-gradient(180deg, var(--bg-top), var(--bg-bottom));
    font-family: "Open Sans", Arial, sans-serif;
    color: var(--text);
    position: relative;
  }
  .page {
    position: absolute; left: 172px; top: 26px; width: 860px; height: 874px;
    background: var(--page); border: 1px solid var(--frame); border-bottom: none;
  }
  .page-topline {
    position: absolute; left: 17px; top: 2px; width: 826px; height: 3px;
    background: linear-gradient(180deg, #e4e4e4, #f7f7f7);
  }
  .brand {
    position: absolute; left: 25px; top: 72px;
    font-size: 22px; line-height: 28px; font-weight: 600; color: var(--ink);
    white-space: nowrap;
  }
  .main-nav { position: absolute; top: 59px; left: 0; width: 100%; }
  .nav-item {
    position: absolute; font-size: 12.2px; color: var(--nav); text-transform: uppercase;
    line-height: 18px; white-space: nowrap;
  }
  .nav-item.is-active { color: var(--accent); }
  .nav-item.is-active::before {
    content: ""; position: absolute; left: 0; right: 0; top: -2px; height: 2px; background: var(--accent);
  }
  .dropdown {
    position: absolute; left: 442px; top: 77px; width: 191px; height: 165px;
    background: var(--page); border: 1px solid #bdbdbd; z-index: 5; padding-top: 5px;
  }
  .dropdown li {
    list-style: none; font-size: 12.2px; color: var(--nav); line-height: 26px; padding-left: 8px; white-space: nowrap;
  }
  .hero {
    position: absolute; left: 25px; top: 137px; width: 809px; height: 301px;
    background:
      linear-gradient(180deg, rgba(0,0,0,0) 55%, rgba(20,22,22,0.85) 100%),
      linear-gradient(100deg, #a9b2ae 0%, #cfd2c9 35%, #e6d9c6 65%, #d9c1a6 100%);
  }
  .welcome { position: absolute; left: 25px; top: 464px; width: 809px; text-align: center; }
  .welcome h1 { font-size: 16px; font-weight: 600; color: var(--ink); letter-spacing: 0.4px; line-height: 22px; }
  .welcome p {
    font-size: 10.9px; line-height: 17px; margin-top: 2px; padding: 0 2px;
    letter-spacing: -0.05px; hyphens: auto;
  }
  .divider {
    position: absolute; left: 25px; top: 584px; width: 809px; height: 10px;
    border-top: 1px solid var(--rule);
    background: linear-gradient(180deg, #f1f1f1, rgba(255,255,255,0));
  }
  .cta {
    position: absolute; left: 381px; top: 566px; width: 97px; height: 36px;
    background: linear-gradient(180deg, #fbfbfb, #e9e9e9); border: 1px solid #c9c9c9; border-radius: 2px;
    font-family: Arial, Helvetica, sans-serif; font-size: 11px; font-weight: 700; color: #333;
    text-align: center; line-height: 34px; box-shadow: 0 1px 2px rgba(0,0,0,0.12);
  }
  .feature { position: absolute; top: 647px; width: 250px; }
  .feature-badge {
    position: absolute; left: 0; top: 0; width: 31px; height: 31px; border-radius: 50%;
    background: var(--badge); border: 2px solid #fff; box-shadow: 0 0 0 1.5px var(--badge);
    color: #fff; font-size: 16px; line-height: 27px; text-align: center;
  }
  .feature h2 {
    position: absolute; left: 42px; top: 3px; font-size: 15.5px; font-weight: 600; color: var(--ink); line-height: 24px;
  }
  .feature p {
    position: absolute; left: 43px; top: 33px; width: 205px; font-size: 10.6px; line-height: 17.2px;
    color: var(--text); hyphens: auto;
  }
  .feature .read-more {
    position: absolute; left: 42px; top: 119px; font-size: 11px; color: var(--accent); text-decoration: none;
  }
  .footer-edge {
    position: absolute; left: 0; top: 838px; width: 100%; height: 16px;
    background: repeating-linear-gradient(135deg, #f3f3f3 0 2px, #fafafa 2px 4px);
  }
  .footer { position: absolute; left: 0; top: 854px; width: 100%; height: 20px; background: var(--footer); }
</style>
</head>
<body>
  <div class="page">
    <div class="page-topline"></div>

    <header>
      <div class="brand">Arbor Group</div>
      <nav class="main-nav">
        <span class="nav-item is-active" style="left:303px">Home</span>
        <span class="nav-item" style="left:361px">About Us</span>
        <span class="nav-item" style="left:442px">About Companies</span>
        <span class="nav-item" style="left:578px">Careers</span>
        <span class="nav-item" style="left:650px">Enquiry Form</span>
        <span class="nav-item" style="left:761px">Contact Us</span>
      </nav>
      <ul class="dropdown">
        <li>ARBOR REAL ESTATE</li>
        <li>VANTECT</li>
        <li>ARBTECH</li>
        <li>ARBOR MORTGAGE BROKERS</li>
        <li>A.CON</li>
        <li>ARBOR TELECOM</li>
      </ul>
    </header>

    <div class="hero" role="img" aria-label="Photograph of a city skyline of business towers silhouetted against a hazy evening sky"></div>

    <section class="welcome">
      <h1>WELCOME TO ARBOR GROUP</h1>
      <p>Arbor is synonymous with innovation and quality. We aim to be an intergral part of the lves of our customers, providing them with convenience and flexibility. By evaluatuing their needs and designing solutions to cater to these needs, Arbor aims to remain responsible, original and ahead of times. In an increasingly con&shy;nected worlds, Arbor has always been a pioneer in introducing unique value added services and outsourcing solutions to the Middle Eastern consumer</p>
    </section>

    <div class="divider"></div>
    <div class="cta">ENQUIRE NOW</div>

    <section class="feature" style="left:25px">
      <div class="feature-badge">1</div>
      <h2>Our Vision</h2>
      <p>To be a regionally renowned, market-focused, customer centred brand that delivers technologically innovative solu&shy;tions with excellent value for customers</p>
      <a class="read-more" href="#">Read more &gt;</a>
    </section>
    <section class="feature" style="left:300px">
      <div class="feature-badge">2</div>
      <h2>Our Mission</h2>
      <p>We are a market-focused, process-centered organization that develops and delivers innovative solutions to our cus&shy;tomers, consistently outperforms our</p>
      <a class="read-more" href="#">Read more &gt;</a>
    </section>
    <section class="feature" style="left:575px">
      <div class="feature-badge">3</div>
      <h2>Our Divisions</h2>
      <p>We have variation sub-divisions of Arbor Group, we provide any services that you want so we can easily help you out from your problem and give you the solutions.</p>
      <a class="read-more" href="#">Read more &gt;</a>
    </section>

    <div class="footer-edge"></div>
    <footer class="footer"></footer>
  </div>
</body>
</html>
```